依頼詳細
デザインを依頼する製品の名前は「雲居そば」です。
表面のデザイン作成をお願いします。

【デザインイメージ】
・シックで高級感のあるデザインが好ましいです。
・希望の色はベースが黒色で商品名の「雲居そば」は金色でお願いします。

【必須記載事項】
下記の文言は必ずデザイン上に記載をお願いします。
・ゆで時間4~5分
・内容量220g
・「謹製」(四角の判子風)
・「本場信州の伝統の味」
・「そばの豊かな香りと喉ごしの良さを楽しめます」

【その他製品特徴】
下記はその他製品の特徴になります。デザインへの記載は各ランサー様へお任せします。
・本品「雲居そば」は、本場信州の恵まれた気候風土と長年の経験の中から独自の製法を編み出し、生まれました。のどごしの良いなめらかな食感と風味豊かな香りを楽しめるそばに仕上げました。
・本品は贈答品で使用することが多いため、化粧箱に入っている状態で見栄えが良く見えるデザインをお願いします。また参考となる画像を添付いたします。
記載項目
製品サイズ(実寸):295×75(mm)
希望イメージ
シンプル 複雑
単色 カラフル
暗い 明るい
日常 高級
遊び心 厳粛
未来的 伝統的
女性的 男性的
希望する色
無彩色系
納品ファイル
• 高解像度JPG (.jpg)
• イラストレーター形式 (.ai)

当社がイメージした通り、シックで高級感があり化粧箱に入っている状態で見栄えが良く見えるデザインで、社内のアンケートでも好評だったため選定させていただきました。

この度は、たくさんのご提案を頂き、大変ありがとうございます。
さまざまなデザイン案やコンセプトがあり、選考に時間をいただいてしまいました。
提案者の皆様の非常にクオリティの高い提案に加え、さまざまな方向性のデザインがありとても良い勉強になりました。

```html
<!DOCTYPE html>
<html lang="ja">
<head>
<meta charset="utf-8">
<title>雲居そば パッケージ表面</title>
<link rel="stylesheet" href="https://fonts.googleapis.com/css2?family=Yuji+Boku&family=Shippori+Mincho:wght@500;700&display=swap">
<style>
  :root {
    --paper: #ffffff;
    --ink: #0b0706;
    --crimson: #7a1712;
    --crimson-deep: #3a0a08;
    --gold-light: #f6e3b0;
    --gold: #d4b06a;
    --gold-dark: #9a7636;
    --silver: #cfc9c2;
    --seal: #b3241c;
  }
  * { margin: 0; padding: 0; box-sizing: border-box; }
  html, body { width: 1200px; height: 2888px; overflow: hidden; background: var(--paper); }
  .package {
    position: absolute; left: 32px; top: 48px; width: 1136px; height: 2800px;
    background: var(--ink); overflow: hidden;
  }
  .pattern-field {
    position: absolute; inset: 0;
    background:
      linear-gradient(180deg, var(--crimson) 0%, var(--crimson-deep) 14%, var(--ink) 27%, var(--ink) 72%, var(--crimson-deep) 86%, var(--crimson) 100%);
  }
  .gold-text {
    background: linear-gradient(180deg, var(--gold-light) 0%, var(--gold) 45%, var(--gold-dark) 70%, var(--gold-light) 100%);
    -webkit-background-clip: text; background-clip: text; color: transparent;
  }
  .catch {
    position: absolute; left: 50%; top: 60px; transform: translateX(-50%);
    writing-mode: vertical-rl; font-family: "Yuji Boku", serif;
    font-size: 76px; letter-spacing: 4px; line-height: 1;
  }
  .product-name { position: absolute; inset: 0; font-family: "Yuji Boku", serif; }
  .product-name span { position: absolute; left: 50%; transform: translateX(-50%); line-height: 1; }
  .pn-1 { top: 740px; font-size: 330px; }
  .pn-2 { top: 1110px; font-size: 330px; }
  .pn-3 { top: 1470px; font-size: 400px; }
  .pn-4 { top: 1880px; font-size: 520px; }
  .tagline {
    position: absolute; left: 320px; top: 1020px; height: 1380px;
    display: flex; flex-direction: column; align-items: center; gap: 24px;
    color: var(--silver); font-family: "Shippori Mincho", serif; font-weight: 500;
  }
  .tagline .rule { width: 2px; flex: 1; background: var(--silver); opacity: .7; }
  .tagline p { writing-mode: vertical-rl; font-size: 48px; letter-spacing: 6px; line-height: 1; }
  .seal {
    position: absolute; left: 748px; top: 2180px; width: 112px; height: 250px;
    border: 8px solid var(--seal); border-radius: 10px; transform: rotate(-4deg);
    color: var(--seal); font-family: "Yuji Boku", serif; font-size: 88px;
    writing-mode: vertical-rl; display: flex; align-items: center; justify-content: center; line-height: 1;
  }
  .spec { position: absolute; left: 8px; width: 460px; height: 86px; display: flex;
    border: 3px solid var(--gold); font-family: "Shippori Mincho", serif; font-weight: 700; font-size: 44px; }
  .spec-1 { top: 2352px; }
  .spec-2 { top: 2480px; }
  .spec dt { width: 210px; display: flex; align-items: center; justify-content: center;
    background: linear-gradient(180deg, var(--gold-light), var(--gold)); color: var(--ink); }
  .spec dd { flex: 1; display: flex; align-items: center; justify-content: center; color: var(--gold-light); }
  .sparkles { position: absolute; inset: 0; }
</style>
</head>
<body>
<main class="package">
  <div class="pattern-field" role="img" aria-label="黒地に深紅のグラデーションと和柄の麻の葉文様"></div>

  <svg class="sparkles" width="1136" height="2800" viewBox="0 0 1136 2800" aria-hidden="true">
    <g fill="#e8cf8e">
      <circle cx="880" cy="560" r="6"/><circle cx="300" cy="690" r="5"/>
      <circle cx="980" cy="880" r="7"/><circle cx="180" cy="1150" r="5"/>
      <circle cx="1020" cy="1300" r="6"/><circle cx="240" cy="1620" r="6"/>
      <circle cx="960" cy="1760" r="5"/><circle cx="880" cy="2160" r="6"/>
      <circle cx="460" cy="2180" r="5"/><circle cx="1000" cy="2560" r="6"/>
    </g>
  </svg>

  <h2 class="catch gold-text">本場信州の伝統の味</h2>

  <h1 class="product-name" aria-label="雲居そば">
    <span class="pn-1 gold-text">雲</span>
    <span class="pn-2 gold-text">居</span>
    <span class="pn-3 gold-text">そ</span>
    <span class="pn-4 gold-text">ば</span>
  </h1>

  <div class="tagline">
    <span class="rule"></span>
    <p>そばの豊かな香りと喉ごしの良さを楽しめます</p>
    <span class="rule"></span>
  </div>

  <div class="seal">謹製</div>

  <dl class="spec spec-1"><dt>ゆで時間</dt><dd>4～5分</dd></dl>
  <dl class="spec spec-2"><dt>内容量</dt><dd>220g</dd></dl>
</main>
</body>
</html>
```